Highlight Document Over Image for Slide

We are seeking a graphic designer to overlay a news article on an image that pertains to the article, aiming for a stylish yet professional appearance. Given the limited resources, we encourage you to use your imagination and go beyond what basic tools like PowerPoint can offer.

```html
<!DOCTYPE html>
<html lang="en">
<head>
<meta charset="UTF-8">
<title>Introduction or Possession of Contraband Items</title>
<link href="https://fonts.googleapis.com/css2?family=Lexend:wght@700&family=Montserrat:wght@400&display=swap" rel="stylesheet">
<style>
  :root {
    --page-bg: #efefef;
    --panel: rgba(44, 44, 44, 0.86);
    --text: #ffffff;
    --map-dark: #3c3b36;
    --map-mid: #6b5c45;
    --map-warm: #8a7350;
    --water: #56544d;
  }
  * { margin: 0; padding: 0; box-sizing: border-box; }
  html, body {
    width: 1200px;
    height: 1200px;
    overflow: hidden;
    background: var(--page-bg);
  }
  .slide {
    position: absolute;
    left: 25px;
    top: 242px;
    width: 1155px;
    height: 649px;
    overflow: hidden;
  }
  .slide__backdrop {
    position: absolute;
    inset: 0;
    background:
      radial-gradient(ellipse at 45% 45%, var(--map-mid) 0%, var(--map-dark) 55%, transparent 80%),
      linear-gradient(170deg, var(--map-warm) 0%, var(--map-mid) 20%, var(--map-dark) 55%, var(--water) 100%);
  }
  .slide__panel {
    position: absolute;
    left: 66px;
    top: 65px;
    width: 1024px;
    height: 519px;
    background: var(--panel);
  }
  .slide__title {
    position: absolute;
    left: 0;
    top: 53px;
    width: 100%;
    text-align: center;
    font-family: "Lexend", sans-serif;
    font-weight: 700;
    font-size: 46px;
    line-height: 62px;
    letter-spacing: 0.5px;
    color: var(--text);
    text-transform: uppercase;
  }
  .slide__rule {
    position: absolute;
    left: 85px;
    top: 220px;
    width: 3px;
    height: 213px;
    background: var(--text);
  }
  .slide__body {
    position: absolute;
    left: 115px;
    top: 217px;
    width: 844px;
    font-family: "Montserrat", sans-serif;
    font-weight: 400;
    font-size: 19.5px;
    line-height: 29px;
    letter-spacing: 0.4px;
    text-align: justify;
    color: var(--text);
  }
</style>
</head>
<body>
  <section class="slide">
    <div class="slide__backdrop" role="img" aria-label="Aerial satellite map of a waterfront correctional facility with surrounding roads and bay"></div>
    <div class="slide__panel">
      <h1 class="slide__title">Introduction or Possession of<br>Contraband Items</h1>
      <span class="slide__rule"></span>
      <p class="slide__body">Employees shall not introduce or possess unauthorized items such as escape paraphernalia, weapons, facsimiles of weapons, ammunition, wireless communication devices, cell phones, tobacco or facsimiles of tobaccos products (e.g. electronic vapor cigarettes) lighters or any other item not specifically authorized by PD 04.04.100 “Custody, Security and Safety Systems (Exempt)”, OP 04.04.100 “Gate Security” or facility operating procedure in any facility where offenders are housed. Employees are responsible for any item in their</p>
    </div>
  </section>
</body>
</html>
```